Under Lanterns to ORCHARDS - Transformative guide on Optimizing your health, body, and mind.

PLEASE READ: My book is all about optimizing a person's health.
Most people go through life in pain, low energy, disappointed with their body and living a short life relying on medication. I call this "Surviving"

My Goal is to transform their life from serving to THRIVING. This is why you see the background I these images as a cold, dark cracking desert. From this cold dark desert I want there to be a thriving and emerging plant brain like the one seen on image #1. I also want my readers to pick up the book and know that the book is about humans. So I want there to be a nervous system like in image #2 Lastly on image 3. I want there to be consistency throughout the whole book. Like the cracking desert in the background of the back cover.

Target Market(s)

People struggling with their health

Industry/Entity Type

Health

Colors
0054AA
0677BA
7BADD7
CADEEF
E8F1F8
00AB8E
00BBA5
67D7C9
C6EFE9
E9F9F6

Requirements
Must have
• Brain, and Nervous system.
Nice to have
• Colors selected

```html
<!DOCTYPE html>
<html lang="en">
<head>
<meta charset="utf-8">
<title>Under Lanterns to Orchards — Book Cover</title>
<link rel="stylesheet" href="https://fonts.googleapis.com/css2?family=Bebas+Neue&family=Great+Vibes&family=Montserrat:wght@600;700&display=swap">
<style>
  :root {
    --page-bg: #f3f3f3;
    --cover-bg: #141319;
    --title-blue: #0a77c2;
    --title-orange: #f07f2e;
    --ink-white: #ffffff;
    --glow-blue: #2f7fc4;
    --glow-orange: #f2953e;
    --deep-navy: #10203a;
  }
  * { margin: 0; padding: 0; box-sizing: border-box; }
  html, body {
    width: 1200px;
    height: 1200px;
    overflow: hidden;
    background: var(--page-bg);
  }
  .canvas {
    position: relative;
    width: 1200px;
    height: 1200px;
    display: flex;
    align-items: center;
    justify-content: center;
  }
  .cover {
    position: relative;
    width: 740px;
    height: 1140px;
    background: var(--cover-bg);
    overflow: hidden;
    color: var(--ink-white);
    text-align: center;
  }
  .kicker {
    position: absolute;
    top: 62px;
    left: 0;
    right: 0;
    display: flex;
    align-items: center;
    justify-content: center;
    gap: 22px;
    font-family: "Bebas Neue", sans-serif;
    font-size: 86px;
    line-height: 1;
  }
  .kicker-rule {
    width: 200px;
    height: 3px;
    background: var(--ink-white);
  }
  .title {
    position: absolute;
    top: 140px;
    left: 0;
    right: 0;
    font-family: "Bebas Neue", sans-serif;
    font-weight: 400;
    line-height: 0.86;
  }
  .title-line {
    display: block;
    font-size: 196px;
    letter-spacing: -1px;
  }
  .title-first { color: var(--title-blue); }
  .title-second { color: var(--title-orange); margin-top: 18px; }
  .title-joiner {
    position: absolute;
    top: 128px;
    left: 0;
    right: 0;
    font-family: "Great Vibes", cursive;
    font-size: 86px;
    color: var(--ink-white);
    line-height: 1;
  }
  .subtitle {
    position: absolute;
    top: 540px;
    left: 40px;
    right: 40px;
    font-family: "Montserrat", sans-serif;
    font-weight: 600;
    font-size: 23px;
    line-height: 1.3;
    text-transform: uppercase;
    letter-spacing: 0.3px;
  }
  .artwork {
    position: absolute;
    top: 620px;
    left: 0;
    width: 740px;
    height: 390px;
    background:
      radial-gradient(ellipse 170px 150px at 46% 42%, rgba(242,149,62,0.75), rgba(242,149,62,0) 70%),
      radial-gradient(ellipse 250px 200px at 50% 45%, rgba(47,127,196,0.7), rgba(47,127,196,0) 75%),
      radial-gradient(ellipse 420px 260px at 50% 50%, var(--deep-navy), var(--cover-bg) 85%);
  }
  .author {
    position: absolute;
    bottom: 48px;
    left: 0;
    right: 0;
    font-family: "Montserrat", sans-serif;
    font-weight: 700;
    font-size: 46px;
    letter-spacing: 12px;
    text-transform: uppercase;
  }
</style>
</head>
<body>
  <main class="canvas">
    <article class="cover">
      <div class="kicker">
        <span class="kicker-rule"></span>
        <span class="kicker-word">Under</span>
        <span class="kicker-rule"></span>
      </div>

      <h1 class="title">
        <span class="title-line title-first">Lanterns</span>
        <span class="title-line title-second">Orchards</span>
      </h1>
      <span class="title-joiner">to</span>

      <p class="subtitle">Transformative guide on optimizing<br>your health, body, and mind</p>

      <div class="artwork" role="img" aria-label="Illustration of a glowing human head in profile with a luminous brain and nervous system against a starry night sky"></div>

      <p class="author">Author Name</p>
    </article>
  </main>
</body>
</html>
```